Packaging Design Project

We need a packaging design for a portable solar charger and 3-way cable.
The package style that is added in the pictures is preferred but we are open to suggestions.
I also added the cut line for the paper with fold lines

Industry/Entity Type

Solar

```html
<!DOCTYPE html>
<html lang="en">
<head>
<meta charset="utf-8">
<title>Solar Charger Packaging – Front and Back Panels</title>
<link href="https://fonts.googleapis.com/css2?family=Didact+Gothic&display=swap" rel="stylesheet">
<style>
  :root {
    --stage: #e9e9ea;
    --panel-black: #0b0b0c;
    --panel-charcoal: #2a2a2c;
    --panel-grey: #3b3b3e;
    --silver: #d9d9dc;
    --silver-dark: #8c8c90;
    --text-light: #e6e6e8;
    --text-soft: #bdbdc1;
  }
  * { box-sizing: border-box; margin: 0; padding: 0; }
  html, body {
    width: 1200px; height: 900px; overflow: hidden;
    background: var(--stage);
    font-family: "Didact Gothic", "Helvetica Neue", Arial, sans-serif;
  }
  .layout {
    position: relative; width: 1200px; height: 900px;
    display: flex; align-items: center; justify-content: center; gap: 60px;
  }
  .panel {
    position: relative; width: 540px; height: 540px; overflow: hidden;
    background: linear-gradient(135deg, var(--panel-charcoal) 0%, var(--panel-black) 55%, var(--panel-black) 100%);
    box-shadow: 0 10px 30px rgba(0,0,0,.25);
  }
  .panel__swoosh { position: absolute; inset: 0; width: 100%; height: 100%; }

  /* Front panel */
  .product-photo {
    position: absolute; left: 150px; top: 70px; width: 250px; height: 270px;
    border-radius: 26px;
    background: radial-gradient(circle at 35% 30%, #4a4a4e 0%, #1c1c1e 60%, #101011 100%);
    border: 3px solid var(--silver-dark);
  }
  .front-title {
    position: absolute; left: 38px; bottom: 58px; color: var(--text-light);
    transform: rotate(-14deg); transform-origin: left bottom;
  }
  .front-title__main { display: block; font-size: 64px; letter-spacing: 4px; line-height: 1; }
  .front-title__sub { display: block; font-size: 34px; line-height: 1.1; margin-left: 2px; }

  /* Back panel */
  .spec-list {
    position: absolute; right: 36px; top: 86px; list-style: none; text-align: right;
    color: var(--text-soft); font-size: 15px; line-height: 34px;
  }
  .compliance {
    position: absolute; left: 24px; bottom: 30px; display: flex; align-items: center; gap: 8px;
  }
  .compliance__mark { width: 16px; height: 16px; background: var(--silver); }
  .compliance__mark--round { border-radius: 50%; background: #6faa4a; }
  .compliance__origin { color: var(--text-soft); font-size: 7px; letter-spacing: .5px; margin-left: 2px; }
</style>
</head>
<body>
<main class="layout">

  <section class="panel panel--front" aria-label="Front panel">
    <svg class="panel__swoosh" viewBox="0 0 540 540" aria-hidden="true">
      <path d="M540 0 L330 0 C180 90 150 300 300 540 L540 540 Z" fill="#1a1a1c"/>
      <path d="M420 0 C250 80 190 300 330 540" fill="none" stroke="#d9d9dc" stroke-width="4"/>
      <path d="M440 0 C280 90 230 300 360 540" fill="none" stroke="#4a4a4e" stroke-width="2"/>
    </svg>
    <div class="product-photo" role="img" aria-label="Photograph of the black square solar charger with a dock connector on top"></div>
    <h1 class="front-title">
      <span class="front-title__main">SOLAR</span>
      <span class="front-title__sub">with USB hub</span>
    </h1>
  </section>

  <section class="panel panel--back" aria-label="Back panel">
    <svg class="panel__swoosh" viewBox="0 0 540 540" aria-hidden="true">
      <circle cx="430" cy="270" r="330" fill="#1d1d1f"/>
      <path d="M250 -5 A330 330 0 0 0 210 520" fill="none" stroke="#d9d9dc" stroke-width="5"/>
      <path d="M0 540 L0 330 C60 420 140 500 260 540 Z" fill="#242426"/>
    </svg>
    <ul class="spec-list">
      <li>Capacity: 2200 mAh</li>
      <li>Input 5V-0.5A</li>
      <li>Output 5V-0.5A</li>
      <li>Charging time 3hours</li>
      <li>Standby time up to 230 hours</li>
      <li>Internet/Talktime up to 4 hours on 3G</li>
      <li>Audio play up to 18 hours</li>
      <li>Video play up to 5 hours</li>
    </ul>
    <div class="compliance">
      <span class="compliance__mark"></span>
      <span class="compliance__mark"></span>
      <span class="compliance__mark compliance__mark--round"></span>
      <span class="compliance__origin">MADE IN CHINA</span>
    </div>
  </section>

</main>
</body>
</html>
```